The Bayfield Wellness Clinic - Practice Flyer

We need a flyer that generally advertises our services. I've uploaded one old flyer as well as examples of others. I like the style of the materials made by this practice: https://www.facebook.com/PineRidgeCounselingHouse

```html
<!DOCTYPE html>
<html lang="en">
<head>
<meta charset="utf-8">
<title>The Bayfield Wellness Clinic – Practice Flyer</title>
<link href="https://fonts.googleapis.com/css2?family=Poppins:ital,wght@0,400;0,500;1,400;1,600&family=Cinzel:wght@400;600&family=Cormorant+Garamond:wght@500&display=swap" rel="stylesheet">
<style>
  :root {
    --olive: #999a61;
    --olive-text: #9b9c5f;
    --forest: #2e4529;
    --pale: #e6e7da;
    --hex: #d8dbc6;
    --ink: #1f1f1f;
    --white: #ffffff;
  }
  * { margin: 0; padding: 0; box-sizing: border-box; }
  html, body { width: 927px; height: 1200px; overflow: hidden; background: var(--white); }
  .flyer { position: relative; width: 927px; height: 1200px; font-family: "Poppins", sans-serif; color: var(--ink); overflow: hidden; }
  .abs { position: absolute; }

  .brand-mark { left: 108px; top: 53px; width: 114px; height: 114px; border-radius: 50%; background: var(--olive); }
  .brand-name { left: 233px; top: 72px; width: 620px; font-family: "Poppins", sans-serif; font-weight: 500; font-size: 40px; line-height: 1.15; color: var(--forest); text-align: center; }
  .brand-sub { left: 233px; top: 148px; width: 620px; font-family: "Poppins", sans-serif; font-weight: 500; font-size: 14px; letter-spacing: 3px; color: var(--forest); text-align: center; }

  .intro { font-style: italic; color: var(--olive-text); white-space: nowrap; }
  .intro .name { font-family: "Cinzel", serif; font-style: normal; font-size: 17px; }
  .intro strong { font-weight: 600; }
  .intro-main { left: 55px; top: 192px; font-size: 18px; line-height: 22.6px; }
  .intro-second { left: 55px; top: 330px; font-size: 16.5px; line-height: 19.7px; }
  .intro-cbt { left: 491px; top: 690px; font-size: 16.5px; line-height: 19.7px; }

  .band { background: var(--olive); color: var(--white); font-family: "Cinzel", serif; font-weight: 400; font-size: 20px; line-height: 27px; height: 27px; }
  .band-expertise { left: 0; top: 421px; width: 515px; padding-left: 55px; }
  .band-treatment { left: 455px; top: 800px; width: 472px; padding-left: 36px; }

  .list { list-style: none; font-size: 15px; line-height: 16.6px; }
  .list li { position: relative; padding-left: 13px; margin-bottom: 4.7px; }
  .list li::before { content: ""; position: absolute; left: 1px; top: 5px; width: 5px; height: 5px; border: 1px solid var(--olive); transform: rotate(45deg); }
  .list .wrap { display: block; padding-left: 11px; }
  .list-left { left: 58px; top: 455px; width: 200px; }
  .list-right { left: 281px; top: 455px; width: 200px; }
  .list-treatment { left: 494px; top: 836px; width: 420px; }

  .photo-cluster { left: 470px; top: 215px; }
  .team-photo { left: 50px; top: 625px; }

  .footer-swoosh { left: 0; top: 990px; }
  .credentials { left: 55px; top: 1051px; font-size: 15px; line-height: 21.5px; }
  .credentials .sep { color: var(--olive); }
  .website { left: 52px; top: 1132px; font-family: "Cormorant Garamond", serif; font-weight: 500; font-size: 24px; color: var(--olive-text); }
  .social { left: 478px; top: 1140px; display: flex; gap: 15px; }
  .social span { display: block; width: 22px; height: 22px; border-radius: 50%; background: var(--olive); }
  .phone { left: 641px; top: 1120px; width: 232px; height: 41px; border-radius: 21px; background: var(--olive); color: var(--white); font-size: 22px; line-height: 41px; display: flex; align-items: center; gap: 10px; padding-left: 18px; }
</style>
</head>
<body>
<div class="flyer">

  <div class="abs brand-mark" aria-hidden="true"></div>
  <div class="abs brand-name">The Bayfield Wellness Clinic</div>
  <div class="abs brand-sub">OF GREATER PHILADELPHIA LLC</div>

  <p class="abs intro intro-main"><span class="name">The Bayfield Wellness Clinic of Greater</span><br><span class="name">Philadelphia (BWC)</span> provides expert clinical care for<br><strong>anxiety disorders</strong>, <strong>obsessive compulsive and related</strong><br><strong>disorders</strong> and <strong>neurodevelopmental disorders</strong><br>in children, adolescents, and adults.</p>

  <p class="abs intro intro-second"><span class="name">BWC</span> proudly provides the Greater<br>Philadelphia community with state-of-the-art<br>assessment and evidence-based therapy for<br>many disorders.</p>

  <h2 class="abs band band-expertise">Our Areas of Expertise:</h2>

  <ul class="abs list list-left">
    <li>Obsessive Compulsive <span class="wrap">Disorder</span></li>
    <li>Trichotillomania</li>
    <li>Excoriation Disorder</li>
    <li>Generalized Anxiety <span class="wrap">Disorder</span></li>
    <li>Panic Disorder</li>
    <li>Specific Phobias</li>
  </ul>
  <ul class="abs list list-right">
    <li>Hoarding Disorder</li>
    <li>Body Dysmorphic <span class="wrap">Disorder</span></li>
    <li>Tic Disorders</li>
    <li>ADHD</li>
    <li>Learning Disorders</li>
    <li>Insomnia</li>
    <li>Social Anxiety Disorder</li>
  </ul>

  <svg class="abs photo-cluster" width="440" height="445" viewBox="0 0 440 445">
    <polygon points="208,70 330,140 330,300 208,370 86,300 86,140" fill="var(--hex)"/>
    <g stroke="var(--white)" stroke-width="5">
      <circle cx="208" cy="81" r="70" fill="#8c8784" role="img" aria-label="Photo of a stressed man in a suit holding his forehead"/>
      <circle cx="85" cy="150" r="70" fill="#b89b86" role="img" aria-label="Photo of a boy writing at a school desk"/>
      <circle cx="332" cy="153" r="70" fill="#6aa6c8" role="img" aria-label="Photo of a smiling schoolboy with a backpack"/>
      <circle cx="85" cy="296" r="70" fill="#9a8a6a" role="img" aria-label="Photo of a smiling family outdoors"/>
      <circle cx="332" cy="296" r="70" fill="#e6d8cc" role="img" aria-label="Photo of a woman resting her head on her arms"/>
      <circle cx="208" cy="367" r="70" fill="#cdb7a0" role="img" aria-label="Photo of hands being washed with soap"/>
    </g>
  </svg>

  <svg class="abs team-photo" width="420" height="420" viewBox="0 0 420 420">
    <circle cx="212" cy="210" r="203" fill="var(--hex)"/>
    <circle cx="204" cy="205" r="200" fill="#b9b4a4" role="img" aria-label="Photo of a group placing sticky notes on a bright window"/>
  </svg>

  <p class="abs intro intro-cbt"><span class="name">BWC</span> clinicians are highly trained<br>in <strong>cognitive behavioral therapy</strong> (CBT), which<br>includes scientifically informed techniques<br>that are tailored to each client’s unique<br>needs.</p>

  <h2 class="abs band band-treatment">Treatment We Provide:</h2>

  <ul class="abs list list-treatment">
    <li>Cognitive Behavioral Therapy (CBT)</li>
    <li>Exposure and Response Prevention (E/RP)</li>
    <li>Comprehensive Behavioral (ComB)/ <span class="wrap">Habit Reversal Training (HRT)</span></li>
    <li>Cognitive Behavioral Intervention for Tics (CBIT)</li>
    <li>Acceptance and Commitment Therapy (ACT)</li>
    <li>Organizational Skills Training (OST)</li>
    <li>CBT for Insomnia (CBT-I)</li>
  </ul>

  <svg class="abs footer-swoosh" width="927" height="210" viewBox="0 0 927 210" aria-hidden="true">
    <path d="M927,0 C760,80 420,125 0,130 L0,210 L927,210 Z" fill="var(--pale)"/>
    <path d="M927,95 C700,112 350,122 0,124 L0,132 C350,130 700,124 927,108 Z" fill="var(--olive)"/>
  </svg>

  <div class="abs credentials">
    <p>Helen R. Ostrander, PsyD <span class="sep">◇</span> Executive Director Licenced Clinical Psychologist</p>
    <p>New Jersey Lic. No 35SI0071624 <span class="sep">◇</span> Penssylvania Lic. No. PS0183452</p>
  </div>

  <div class="abs website">www.TheBayfieldWellnessClinic.com</div>
  <div class="abs social" aria-label="Social media">
    <span></span><span></span><span></span><span></span>
  </div>
  <div class="abs phone">
    <svg width="24" height="24" viewBox="0 0 24 24" aria-hidden="true"><path d="M6.6 10.8c1.4 2.8 3.8 5.1 6.6 6.6l2.2-2.2c.3-.3.7-.4 1-.2 1.1.4 2.3.6 3.6.6.6 0 1 .4 1 1V20c0 .6-.4 1-1 1C10.6 21 3 13.4 3 4c0-.6.4-1 1-1h3.5c.6 0 1 .4 1 1 0 1.3.2 2.5.6 3.6.1.3 0 .7-.2 1z" fill="none" stroke="var(--white)" stroke-width="1.6"/></svg>
    <span>(856) 555-0148</span>
  </div>

</div>
</body>
</html>
```